Bright Summit Web Design

I am starting a new company that will provide LIFE COACHING services - I have tried to design a website, but it's too complicated. Right now, it's just me - I'm the only person that will provide services through the website - I have used makerhive to purchase a logo (see below). I want to be able to update the website myself, but need a template - basic design. Because I am not technologically savvy enough to explain in words - I basically want to have a website that will provide basic information about my services (coaching), a page about me and my background, hopefully scheduling possibilities, and testimonials — also a page for writing/blogs. I bought a website through NetBarn - so when I have a template, I guess I”d use that - but maybe I’ll need to work with a designer to actually get it up on the internet. I have a head shot that I’ll upload, too.
Clients from the independent (private school) world - teachers, administrators
4 page

```html
<!DOCTYPE html>
<html lang="en">
<head>
<meta charset="utf-8">
<title>Bright Summit Coaching – About Me</title>
<link href="https://fonts.googleapis.com/css2?family=Fredoka:wght@500;600&family=Mulish:wght@400;600;700&display=swap" rel="stylesheet">
<style>
:root{
  --teal:#0e9a8a;
  --mint:#c6eee8;
  --ink:#0d4d47;
  --deep:#0b4a45;
  --text:#3c4a48;
  --white:#ffffff;
  --badge:#27567a;
  --badge-ring:#17a2c4;
}
*{margin:0;padding:0;box-sizing:border-box}
html,body{width:1200px;height:1200px;overflow:hidden;background:var(--white)}
.stage{position:absolute;left:0;top:0;width:1932px;height:1932px;transform:scale(.6211);transform-origin:0 0;font-family:"Mulish",sans-serif;color:var(--text)}
.abs{position:absolute}
.display{font-family:"Fredoka",sans-serif;font-weight:600;color:var(--ink)}
.nowrap{white-space:nowrap}
.header{left:736px;top:0;width:528px;height:62px;background:var(--white)}
.brand-ring{left:766px;top:8px;width:46px;height:46px;border:1.5px solid var(--teal);border-radius:50%}
.brand-name{font-family:"Mulish",sans-serif;font-weight:600;color:var(--ink);font-size:6.5px;white-space:nowrap}
.nav a{position:absolute;top:27px;font-size:5.6px;font-weight:700;color:var(--teal);text-decoration:none;white-space:nowrap}
.phone{left:1076px;top:27px;font-size:5.6px;font-weight:700;color:var(--teal)}
.btn-book{left:1152px;top:19px;width:78px;height:23px;background:var(--teal);color:var(--white);font-size:5.6px;font-weight:700;display:flex;align-items:center;justify-content:center;border-radius:1px}
.hero-photo{left:736px;top:62px;width:264px;height:178px;background:linear-gradient(100deg,#8d7766 0%,#d9cfc4 30%,#c8a27f 50%,#3a3a3a 75%,#ece7e1 100%)}
.hero-panel{left:1000px;top:62px;width:264px;height:178px;background:var(--mint)}
.hero-title{left:1000px;width:182px;top:131px;text-align:center;font-size:16px}
.crumb{left:1000px;width:182px;top:161px;text-align:center;font-size:5px;color:var(--ink)}
.eyebrow{font-size:5px;color:var(--ink);letter-spacing:.1px;white-space:nowrap}
.about-title{left:784px;top:312px;font-size:17px}
.body-copy{font-size:6.2px;line-height:11px;color:var(--text)}
.divider{left:784px;top:420px;width:172px;height:1px;background:#e2e8e7}
.stat-num{font-size:16px}
.stat-label{font-size:5.2px;color:var(--ink);white-space:nowrap}
.portrait{left:979px;top:292px;width:236px;height:226px;border-radius:50%;background:radial-gradient(circle at 50% 45%,#e3c9a5 0%,#d6b58f 22%,#f1ece4 45%,var(--teal) 62%)}
.adv-title{left:807px;top:579px;font-size:8.6px;line-height:13px}
.adv-copy{left:807px;top:622px;width:160px;font-size:4.9px;line-height:9px}
.feature-icon{position:absolute}
.feature-title{font-family:"Fredoka",sans-serif;font-weight:600;color:var(--ink);font-size:7px;white-space:nowrap}
.feature-copy{font-size:4.9px;line-height:10px;color:var(--ink)}
.schedule{left:736px;top:705px;width:528px;height:398px;background:var(--mint)}
.sched-eyebrow{left:736px;width:514px;top:806px;text-align:center}
.sched-title{left:736px;width:544px;top:814px;text-align:center;font-size:17.5px;line-height:25px}
.step-num{width:28px;height:20px;border-radius:50%;background:var(--ink);color:var(--white);font-family:"Fredoka",sans-serif;font-weight:600;font-size:11px;display:flex;align-items:center;justify-content:center}
.step-title{font-family:"Fredoka",sans-serif;font-weight:600;color:var(--ink);font-size:7px;line-height:10.5px;text-align:center;width:120px}
.step-copy{font-size:4.9px;line-height:9px;text-align:center;width:120px;color:var(--ink)}
.cert-title{left:736px;width:550px;top:1146px;text-align:center;font-size:13px}
.badge-square{left:833px;top:1193px;width:43px;height:43px;border-radius:3px;background:linear-gradient(180deg,var(--white) 0 60%,var(--badge) 60%);border:1.5px solid #9fb3c4}
.badge-dark{left:985px;top:1194px;width:45px;height:44px;border-radius:4px;background:var(--badge)}
.badge-ring{left:1129px;top:1197px;width:40px;height:40px;border-radius:50%;border:3px solid var(--badge-ring);background:var(--white)}
.footer{left:736px;top:1291px;width:528px;height:206px;background:var(--mint)}
.footer-ring{left:796px;top:1321px;width:70px;height:70px;border:1.5px solid var(--teal);border-radius:50%}
.footer-head{font-family:"Fredoka",sans-serif;font-weight:600;color:var(--ink);font-size:7.6px;white-space:nowrap}
.footer-line{font-size:5.8px;line-height:10px;color:var(--ink);white-space:nowrap}
.legal{left:736px;top:1497px;width:528px;height:38px;background:var(--deep);color:#d9efec;font-size:5.6px;display:flex;align-items:center;justify-content:center}
</style>
</head>
<body>
<div class="stage">

  <header class="abs header"></header>
  <div class="abs brand-ring"></div>
  <div class="abs brand-name" style="left:770px;top:29px">Bright Summit</div>
  <nav class="nav">
    <a style="left:885px">Home</a>
    <a style="left:921px">About</a>
    <a style="left:957px">Services</a>
    <a style="left:1001px">Contact Us</a>
  </nav>
  <div class="abs phone">(+1)555 010 2030</div>
  <a class="abs btn-book">Book a Session</a>

  <div class="abs hero-photo" role="img" aria-label="Photo of two people shaking hands in an office"></div>
  <div class="abs hero-panel"></div>
  <h1 class="abs display hero-title">About Me</h1>
  <div class="abs crumb">Home/About me</div>

  <div class="abs eyebrow" style="left:784px;top:296px">WHAT DO WE OFFER TO PEOPLE</div>
  <h2 class="abs display about-title">About us</h2>
  <p class="abs body-copy" style="left:784px;top:349px;width:192px">In publishing and graphic design, Lorem ipsum is a placeholder text commonly used to demonstrate the visual form of a document or a typeface without relying on meaningful content.</p>
  <div class="abs divider"></div>
  <div class="abs display stat-num" style="left:784px;top:452px">100+</div>
  <div class="abs stat-label" style="left:778px;top:476px">Persons Mentored</div>
  <div class="abs display stat-num" style="left:916px;top:452px">10+</div>
  <div class="abs stat-label" style="left:910px;top:476px">Experienced</div>
  <div class="abs portrait" role="img" aria-label="Head-and-shoulders portrait of the coach on a teal circle"></div>

  <div class="abs eyebrow" style="left:807px;top:565px">WHAT DO WE OFFER TO PEOPLE</div>
  <h3 class="abs display adv-title">Advantages you get after, joining<br>our Life Coaching services!</h3>
  <p class="abs adv-copy">In publishing and graphic design, Lorem ipsum is a placeholder text commonly used to demonstrate the visual form of a document or a typeface without relying on meaningful content.</p>

  <svg class="feature-icon" style="left:1016px;top:572px" width="26" height="22" viewBox="0 0 26 22" fill="none" stroke="#0d4d47" stroke-width="1">
    <rect x="1" y="2" width="24" height="15" rx="1"/><circle cx="13" cy="7" r="2.5"/><path d="M8 17c0-4 2-6 5-6s5 2 5 6M10 21h6M13 17v4"/>
  </svg>
  <div class="abs feature-title" style="left:1054px;top:571px">Coaching</div>
  <p class="abs feature-copy" style="left:1054px;top:584px;width:136px">In publishing and graphic design, Lorem ipsum is a placeholder text</p>

  <svg class="feature-icon" style="left:1014px;top:609px" width="28" height="28" viewBox="0 0 28 28" fill="none" stroke="#0d4d47" stroke-width="1">
    <rect x="4" y="2" width="8" height="6"/><rect x="15" y="1" width="9" height="7"/><circle cx="13" cy="15" r="2.5"/><path d="M8 26v-5c0-2 2-3 5-3s5 1 5 3v5M2 14h4M4 12v4M23 22h4M25 20v4"/>
  </svg>
  <div class="abs feature-title" style="left:1055px;top:613px">Self Confidence</div>
  <p class="abs feature-copy nowrap" style="left:1055px;top:627px">In publishing and graphic design, Lorem ipsum is a placeholder text</p>

  <svg class="feature-icon" style="left:1012px;top:658px" width="30" height="30" viewBox="0 0 30 30" fill="none" stroke="#0d4d47" stroke-width="1">
    <path d="M12 2c6 0 10 2 16 2M6 6c8-2 14 0 20 0"/><circle cx="15" cy="15" r="5"/><path d="M15 12v6M13 14h4M2 22c4 0 7 2 10 2h10c2 0 5-3 6-4M4 27c5 0 8 1 12 1"/>
  </svg>
  <div class="abs feature-title" style="left:1054px;top:664px">Renew your energy</div>
  <p class="abs feature-copy nowrap" style="left:1054px;top:677px">In publishing and graphic design, Lorem ipsum is a placeholder text</p>

  <section class="abs schedule"></section>
  <div class="abs eyebrow sched-eyebrow">WHAT DO WE OFFER TO PEOPLE</div>
  <h2 class="abs display sched-title">Scheduling for Bright Summit<br>Life Coaching Programe</h2>

  <div class="abs step-num" style="left:828px;top:922px">1</div>
  <div class="abs step-title" style="left:784px;top:958px">Apply by Website</div>
  <p class="abs step-copy" style="left:785px;top:982px">In publishing and graphic design, Lorem ipsum is a placeholder text</p>

  <div class="abs step-num" style="left:986px;top:923px">2</div>
  <div class="abs step-title" style="left:940px;top:958px">Verifying &amp; Interview</div>
  <p class="abs step-copy" style="left:942px;top:982px">In publishing and graphic design, Lorem ipsum is a placeholder text</p>

  <div class="abs step-num" style="left:1139px;top:922px">3</div>
  <div class="abs step-title" style="left:1093px;top:958px">Enrollment to<br>Course</div>
  <p class="abs step-copy" style="left:1092px;top:982px">In publishing and graphic design, Lorem ipsum is a placeholder text</p>

  <h2 class="abs display cert-title">Certification</h2>
  <div class="abs badge-square" role="img" aria-label="Leadership practitioner certification badge"></div>
  <div class="abs badge-dark" role="img" aria-label="Certified professional coach badge"></div>
  <div class="abs badge-ring" role="img" aria-label="Coaching federation membership badge"></div>

  <footer class="abs footer"></footer>
  <div class="abs footer-ring"></div>
  <div class="abs brand-name" style="left:801px;top:1351px;font-size:9.5px">Bright Summit</div>

  <div class="abs footer-head" style="left:972px;top:1333px">ADDRESS LINE</div>
  <div class="abs footer-line" style="left:972px;top:1344px">Address comes here,<br>Address comes here.</div>
  <div class="abs footer-head" style="left:1070px;top:1333px">Email Details</div>
  <div class="abs footer-line" style="left:1070px;top:1344px">hello@brightsummit.com</div>
  <div class="abs footer-head" style="left:1070px;top:1374px">Contact Details</div>
  <div class="abs footer-line" style="left:1070px;top:1385px">Address comes here,<br>Address comes here.</div>

  <div class="abs legal">© 2022 All Rights reserved with brightsummit.com</div>
</div>
</body>
</html>
```